QTR PAGE FLYER

I need a flyer/ad local paper ad for URGENT placement. The ad is for Millbrook Vale FC Juniors and a quick solution is required. I have attached a file which details the copy in Headline/Main Copy etc
I am open minded about font and layout the ad must work in a 144mm high/129mm wide format. I happy for relevant images to be inserted balls/goals/grass or vector/ outline images of players.
I NEED THIS NOW....so I would suggest a less is more approach, well laid out and easy to read!
I also need the Junior logo amended to read Seniors in the sash

```html
<!DOCTYPE html>
<html lang="en">
<head>
<meta charset="utf-8">
<title>Millbrook Vale FC Juniors – Join Us</title>
<link href="https://fonts.googleapis.com/css2?family=Bebas+Neue&display=swap" rel="stylesheet">
<style>
  :root {
    --grass-light: #6fb62c;
    --grass-dark: #4f9a1e;
    --panel: #1b1b1b;
    --white: #ffffff;
    --red: #e0302a;
    --yellow: #f5e21a;
  }
  * { margin: 0; padding: 0; box-sizing: border-box; }
  html, body { width: 1075px; height: 1200px; overflow: hidden; background: var(--panel); }
  .flyer {
    position: relative;
    width: 1075px;
    height: 1200px;
    overflow: hidden;
    font-family: "Bebas Neue", "Arial Narrow", sans-serif;
    color: var(--white);
    background: repeating-linear-gradient(90deg,
      var(--grass-light) 0 68px, var(--grass-dark) 68px 136px);
  }
  .grass-shade {
    position: absolute; inset: 0;
    background: radial-gradient(ellipse at 50% 30%, rgba(255,255,255,0.08), rgba(0,0,0,0.18) 80%);
  }
  .club-mark {
    position: absolute; left: 0; top: 150px; width: 100%;
    display: flex; align-items: center; justify-content: center; gap: 16px;
    font-size: 58px; letter-spacing: 1px; color: var(--white);
  }
  .club-mark .dot { width: 34px; height: 34px; border-radius: 50%; background: var(--white); }
  .headline-top {
    position: absolute; top: 308px; width: 100%; text-align: center;
    font-size: 54px; letter-spacing: 1px;
  }
  .headline-arc { position: absolute; left: 0; top: 370px; width: 1075px; height: 160px; }
  .headline-arc text { font-family: "Bebas Neue", sans-serif; font-size: 118px; fill: var(--white); letter-spacing: 3px; }
  .panel-shape { position: absolute; left: 0; top: 0; width: 1075px; height: 1200px; }
  .copy {
    position: absolute; left: 0; top: 562px; width: 100%;
    text-align: center; font-size: 28px; line-height: 36px;
  }
  .copy p { margin: 0; }
  .red { color: var(--red); }
  .yellow { color: var(--yellow); }
  .intro { font-size: 30px; line-height: 40px; }
  .body-text { font-size: 27px; line-height: 36px; margin-top: 2px !important; }
  .join { font-size: 34px; margin-top: 16px !important; line-height: 44px; }
  .small { font-size: 23px; line-height: 27px; }
  .event { margin-top: 24px !important; font-size: 24px; line-height: 27px; }
  .seniors-title { margin-top: 14px !important; font-size: 26px; line-height: 28px; }
</style>
</head>
<body>
<div class="flyer">
  <div class="grass-shade"></div>

  <div class="club-mark"><span class="dot"></span><span>Millbrook Vale FC</span></div>

  <div class="headline-top">LONG LIVE</div>
  <svg class="headline-arc" viewBox="0 0 1075 160" aria-label="The Vale">
    <defs><path id="arc" d="M290,150 Q537,40 790,150"/></defs>
    <text text-anchor="middle"><textPath href="#arc" startOffset="50%">THE VALE</textPath></text>
  </svg>

  <svg class="panel-shape" viewBox="0 0 1075 1200" aria-hidden="true">
    <path d="M0,832 C170,620 380,507 560,507 C760,507 960,600 1075,752 L1075,1200 L0,1200 Z" fill="var(--white)"/>
    <path d="M0,846 C170,632 380,520 560,520 C760,520 960,612 1075,766 L1075,1200 L0,1200 Z" fill="var(--panel)"/>
  </svg>

  <div class="copy">
    <p class="intro red">MILLBROOK VALE FC JUNIORS</p>
    <p class="intro">IS NOW A NOT-FOR-PROFIT-CLUB</p>
    <p class="intro">RUN <span class="yellow">BY THE MEMBERS FOR THE MEMBERS</span></p>
    <p class="body-text">WE OFFER A NURTURING ENVIRONMENT FOR JUNIOR PLAYERS (5-18 YEARS, OF ALL<br>
      LEVELS) TO DEVELOP THEIR FOOTBALLING SKILLS, STAY FIT AND HOPEFULLY MAKE SOME LIFE<br>
      LONG TERM FRIENDS. WE HAVE RECENTLY JOINED NDFA (NORTHERN DISTRICTS FOOTBALL ASSOCIATION) TO<br>
      ALLOW OUR TEAMS (SOCIAL OR SELECTIVE) THE OPTION OF COMPETING AGAINST THE LEADING TEAMS IN THE AREA</p>
    <p class="join yellow">JOIN US!</p>
    <p class="small">REGISTRATIONS FOR NEW AND RETURNING MEMBERS CAN BE COMPLETED ONLINE: AT WWW.KICKREGISTER.COM.AU<br>
      OR<br>
      ALTERNATIVELY PLEASE REGISTER IN PERSON AT ONE OF OUR REGISTRATION DAYS</p>
    <p class="event yellow">DATES: 7TH FEBRUARY OR 14TH FEBRUARY<br>
      TIME: 3PM – 6PM<br>
      PLACE: MILLBROOK VALE RESERVE</p>
    <p class="seniors-title red">SENIORS</p>
    <p class="small">MEN’S &amp; LADIES AA,O35 AND MEN’S O45<br>
      WE ARE ALWAYS LOOKING FOR NEW PLAYERS. IF YOU ARE INTERESTED IN PLAYING PLEASE EMAIL INFO@MVFC.ORG</p>
  </div>
</div>
</body>
</html>
```